Book Cover for Notes on the Quiet River's Far Lamps

I need a book cover for a 6 x 9 paperback titled Notes on the Quiet River's Far Lamps Gathered by Sailors and Weavers Resting in the Valley beyond the Northern Valley. It has to do with consciousness, the mind, incarnation onto Earth, leaving Earth, and the life in the life after this life. I have an idea I'm providing with this description, but I am open to anything that would be striking and stimulating, whether with a book or not. I am the author, T. Warren Blakely. I've added another background idea to see if anyone can do something with it and I've increased the budget.

```html
<!DOCTYPE html>
<html lang="en">
<head>
<meta charset="utf-8">
<title>Notes on the Quiet River's Far Lamps — Book Cover</title>
<link rel="stylesheet" href="https://fonts.googleapis.com/css2?family=Exo+2:wght@300;600;700&display=swap">
<style>
  :root {
    --stage: #6d6e71;
    --stage-light: #8a8b8e;
    --ink-navy: #0e2a44;
    --ink-red: #c0102a;
    --glow: #f4f8fb;
    --mist: #b9ccd9;
    --steel: #5f7f97;
    --deep: #173a57;
    --night: #0c2238;
  }
  * { margin: 0; padding: 0; box-sizing: border-box; }
  html, body {
    width: 1200px;
    height: 1200px;
    overflow: hidden;
  }
  body {
    background: radial-gradient(ellipse at 50% 30%, var(--stage-light), var(--stage) 70%);
    font-family: "Exo 2", sans-serif;
    position: relative;
  }
  .book-cover {
    position: absolute;
    left: 280px;
    top: 120px;
    width: 640px;
    height: 960px;
    overflow: hidden;
    box-shadow: 0 18px 40px rgba(0, 0, 0, 0.35);
  }
  .cover-art {
    position: absolute;
    inset: 0;
    background:
      radial-gradient(circle at 50% 7%, var(--glow) 0, rgba(244, 248, 251, 0.9) 8%, rgba(244, 248, 251, 0) 24%),
      radial-gradient(ellipse 38% 55% at 50% 50%, rgba(185, 204, 217, 0.75), rgba(185, 204, 217, 0) 100%),
      radial-gradient(ellipse 60% 40% at 50% 88%, rgba(214, 228, 238, 0.85), rgba(214, 228, 238, 0) 100%),
      linear-gradient(90deg, var(--night) 0%, var(--deep) 18%, var(--steel) 50%, var(--deep) 82%, var(--night) 100%);
  }
  .cover-text {
    position: absolute;
    inset: 0;
  }
  .title {
    position: absolute;
    left: 158px;
    top: 448px;
    color: var(--ink-navy);
    font-weight: 600;
    font-size: 60px;
    line-height: 0.98;
    letter-spacing: 0.06em;
    text-transform: uppercase;
  }
  .title span { display: block; }
  .title .title-accent {
    color: var(--ink-red);
    font-weight: 700;
  }
  .subtitle {
    position: absolute;
    left: 158px;
    top: 738px;
    width: 440px;
    color: var(--ink-navy);
    font-weight: 300;
    font-size: 21px;
    line-height: 1.3;
  }
  .author {
    position: absolute;
    left: 0;
    right: 0;
    top: 892px;
    text-align: center;
    padding-left: 32px;
    color: var(--ink-navy);
    font-weight: 600;
    font-size: 32px;
  }
</style>
</head>
<body>
  <section class="book-cover">
    <div class="cover-art" role="img" aria-label="Illustration of a luminous figure with head bowed, dissolving into a blue, snow-flecked mist beneath a bright white glow"></div>
    <div class="cover-text">
      <h1 class="title">
        <span>Notes on</span>
        <span>the Quiet</span>
        <span>River's Far</span>
        <span class="title-accent">Lamps</span>
      </h1>
      <p class="subtitle">Gathered by Sailors and Weavers Resting<br>in the Valley beyond the Northern Valley</p>
      <p class="author">T. Warren Blakely</p>
    </div>
  </section>
</body>
</html>
```